Aged Care Consultancy Business needs a business card design

I need a two sided business card - I want it clean and professional. Surprise me

Target Market(s)

middle aged and ageing victorians

Industry/Entity Type

Health Care

Contact Information for Business Card

Text to be included

Logo
Aged Care Consulting Services
Professional, Reliable, Affordable

Tovan Brelsick
Director
0427 31 64 92 (larger)
1300 73 29 41
tovan@wadolire.com.au
www.wadolcare.com.au
Facebook (details TBA)

include little icons beside the contact info:

- Envelope = email
- Phone = phone
- Globe = website

Font styles to use
Serif
Sans Serif

Requirements
Must have
• look proffesional and clean

```html
<!DOCTYPE html>
<html lang="en">
<head>
<meta charset="utf-8">
<title>wadol care – business card</title>
<link href="https://fonts.googleapis.com/css2?family=Cabin:wght@400;500;600&display=swap" rel="stylesheet">
<style>
  :root {
    --navy: #003c78;
    --orange: #e08a00;
    --ink: #3b3b3b;
    --paper: #f7f7f7;
    --backdrop: #4c4c4c;
    --rule: #c9c9c9;
  }
  * { box-sizing: border-box; margin: 0; padding: 0; }
  html, body { width: 1200px; height: 750px; overflow: hidden; }
  body {
    background: var(--backdrop);
    font-family: "Cabin", sans-serif;
    position: relative;
  }
  .card {
    position: absolute;
    top: 228px;
    width: 461px;
    height: 262px;
    border-radius: 12px;
  }
  .card-front { left: 124px; background: var(--paper); }
  .card-back { left: 618px; background: var(--navy); }

  .brand-name {
    position: absolute;
    left: 0;
    width: 239px;
    top: 98px;
    text-align: center;
    font-size: 29px;
    font-weight: 600;
    color: var(--navy);
    letter-spacing: 0.5px;
  }
  .divider {
    position: absolute;
    left: 239px;
    top: 56px;
    width: 1px;
    height: 152px;
    background: var(--rule);
  }
  .person {
    position: absolute;
    left: 258px;
    top: 58px;
  }
  .person-name { font-size: 18px; font-weight: 500; color: var(--navy); line-height: 1.1; }
  .person-role { font-size: 13px; color: var(--orange); margin-top: 1px; }

  .contacts {
    position: absolute;
    left: 262px;
    top: 114px;
    list-style: none;
  }
  .contacts li {
    display: flex;
    align-items: center;
    height: 17.7px;
    font-size: 12px;
    color: var(--ink);
  }
  .contacts li.primary-phone { font-size: 12.5px; }
  .contacts svg { width: 11px; height: 11px; margin-right: 7px; flex: none; fill: var(--navy); }

  .back-name {
    position: absolute;
    left: 0;
    width: 100%;
    top: 88px;
    text-align: center;
    font-size: 58px;
    font-weight: 600;
    color: #ffffff;
    letter-spacing: 1px;
  }
  .tagline {
    position: absolute;
    left: 0;
    width: 100%;
    top: 225px;
    text-align: center;
    font-size: 12.5px;
    color: #ffffff;
  }
</style>
</head>
<body>
  <section class="card card-front">
    <div class="brand-name">wadol care</div>
    <div class="divider"></div>
    <div class="person">
      <div class="person-name">Tovan Brelsick</div>
      <div class="person-role">Director</div>
    </div>
    <ul class="contacts">
      <li class="primary-phone">
        <svg viewBox="0 0 24 24" aria-hidden="true"><path d="M6.6 10.8a15.1 15.1 0 0 0 6.6 6.6l2.2-2.2c.3-.3.7-.4 1-.2 1.1.4 2.3.6 3.6.6.6 0 1 .4 1 1V20c0 .6-.4 1-1 1A17 17 0 0 1 3 4c0-.6.4-1 1-1h3.5c.6 0 1 .4 1 1 0 1.3.2 2.5.6 3.6.1.3 0 .7-.2 1z"/></svg>
        0427 31 64 92
      </li>
      <li>
        <svg viewBox="0 0 24 24" aria-hidden="true"><path d="M6.6 10.8a15.1 15.1 0 0 0 6.6 6.6l2.2-2.2c.3-.3.7-.4 1-.2 1.1.4 2.3.6 3.6.6.6 0 1 .4 1 1V20c0 .6-.4 1-1 1A17 17 0 0 1 3 4c0-.6.4-1 1-1h3.5c.6 0 1 .4 1 1 0 1.3.2 2.5.6 3.6.1.3 0 .7-.2 1z"/></svg>
        1300 73 29 41
      </li>
      <li>
        <svg viewBox="0 0 24 24" aria-hidden="true"><path d="M2 5h20v14H2z M3.5 6.5 12 13l8.5-6.5" fill="none" stroke="#003c78" stroke-width="2"/></svg>
        tovan@wadolire.com.au
      </li>
      <li>
        <svg viewBox="0 0 24 24" aria-hidden="true"><g fill="none" stroke="#003c78" stroke-width="2"><circle cx="12" cy="12" r="9.5"/><ellipse cx="12" cy="12" rx="4" ry="9.5"/><path d="M2.5 12h19"/></g></svg>
        www.wadolcare.com.au
      </li>
      <li>
        <svg viewBox="0 0 24 24" aria-hidden="true"><rect x="3" y="3" width="18" height="18"/></svg>
        wadolcare
      </li>
    </ul>
  </section>

  <section class="card card-back">
    <div class="back-name">wadol care</div>
    <p class="tagline">Aged Care Consulting Services,Professional, Reliable, Affordable</p>
  </section>
</body>
</html>
```